Wellness Flyer

I am seeking a flyer for my health and wellness company, Harbor Bloom. The flyer is to be DL size and single-sided. I am looking for a flyer that is both professional and fun looking, something similar to the uploaded files. Wording to include: (Please not wording to not include company name or logo but is rather advertising nutritional cleansing products)

Be your healthiest self. Take charge of your life. Get your best body.
Lose weight / Build muscle / Gain energy / Increase clarity
Start your journey to health and wellness. Transform your life
www.harborbloomco.com.au
Marisol@harborbloomco.com.au.
Natural . Raw. Organic . Cleansing system

Flyer needs to be single sided, DL size. I haven't uploaded my logo because I wanted to steer clear of having it on the flyer as it limits colour choice. Thanks.

Target Market(s)

Primarily Women 18-50.

Industry/Entity Type

Advertising

Font styles to use
Serif

Colors
34b8a4
fbed24

Requirements
Must have
• The wording as above.
Should not have
• Company name or Company logo

```html
<!DOCTYPE html>
<html lang="en">
<head>
<meta charset="UTF-8">
<title>Harbor Bloom Wellness Flyer</title>
<link href="https://fonts.googleapis.com/css2?family=PT+Sans+Narrow:wght@400;700&family=Open+Sans:wght@400;600&display=swap" rel="stylesheet">
<style>
  :root {
    --backdrop: #f3dba7;
    --cream: #f4f6d8;
    --forest: #0c2a12;
    --forest-mid: #1d4a1c;
    --teal: #34b8a4;
    --teal-deep: #138a6c;
    --teal-band: #2aa886;
    --gold: #f7b718;
    --white: #ffffff;
    --ink: #10261a;
  }
  * { margin: 0; padding: 0; box-sizing: border-box; }
  html, body { width: 1200px; height: 900px; overflow: hidden; }
  body { background: var(--backdrop); position: relative; font-family: "PT Sans Narrow", "Arial Narrow", sans-serif; }

  .flyer {
    position: absolute; left: 395px; top: 20px;
    width: 410px; height: 860px; overflow: hidden;
    background: linear-gradient(180deg, var(--cream) 0%, #eef3cf 40%, #dfe9c3 60%);
    box-shadow: 0 6px 18px rgba(0,0,0,0.25);
  }

  .photo {
    position: absolute; left: 0; top: 175px; width: 410px; height: 450px;
    background: linear-gradient(180deg, rgba(240,244,214,0) 0%, #c9d9cf 30%, #9fbfc2 48%, #8fb98a 68%, #6da43c 85%, #4f8a24 100%);
  }

  .headline-box {
    position: absolute; left: 34px; top: 0; width: 376px; height: 192px;
    border-radius: 0 0 0 26px;
    background: radial-gradient(ellipse at 40% 30%, var(--forest-mid) 0%, var(--forest) 75%);
    padding: 26px 0 0 22px;
  }
  .headline-box p { font-weight: 700; line-height: 1.12; }
  .headline-gold { color: var(--gold); font-size: 38px; }
  .headline-teal { color: var(--teal); font-size: 38px; }
  .headline-big { color: var(--gold); font-size: 44px; }

  .benefits {
    position: absolute; right: 28px; top: 208px; width: 192px;
    list-style: none;
  }
  .benefits li {
    height: 33px; margin-bottom: 6px; border-radius: 4px;
    font-size: 24px; font-weight: 700; color: var(--ink);
    text-align: right; padding-right: 12px; line-height: 33px;
  }
  .benefit-teal { background: var(--teal); }
  .benefit-gold { background: var(--gold); }

  .footer-shape { position: absolute; left: 0; top: 560px; width: 410px; height: 300px; }

  .journey {
    position: absolute; left: 34px; top: 632px; width: 360px;
    color: var(--gold); font-weight: 700; font-size: 29px; line-height: 1.18;
  }
  .transform {
    position: absolute; left: 130px; top: 706px;
    color: var(--white); font-weight: 700; font-size: 29px;
  }
  .divider {
    position: absolute; left: 34px; top: 754px; width: 360px; height: 1px;
    background: rgba(255,255,255,0.25);
  }
  .contact {
    position: absolute; left: 34px; top: 766px; width: 360px; text-align: center;
    font-family: "Open Sans", Arial, sans-serif; font-size: 15px; line-height: 1.3;
    color: #e4efe9;
  }
  .tagline-band {
    position: absolute; left: 0; bottom: 0; width: 410px; height: 46px;
    background: var(--teal-band);
    font-weight: 700; font-size: 22px; color: var(--ink);
    text-align: center; line-height: 46px;
  }
</style>
</head>
<body>
  <article class="flyer">
    <div class="photo" role="img" aria-label="Photo of a smiling woman in a mint tank top stretching on grass beside a river with a city skyline"></div>

    <header class="headline-box">
      <p class="headline-gold">Be your healthiest self</p>
      <p class="headline-teal">Take charge of your life</p>
      <p class="headline-big">Get your best body</p>
    </header>

    <ul class="benefits">
      <li class="benefit-teal">Lose weight</li>
      <li class="benefit-gold">Build muscle</li>
      <li class="benefit-teal">Gain energy</li>
      <li class="benefit-gold">Increase clarity</li>
    </ul>

    <svg class="footer-shape" viewBox="0 0 410 300" aria-hidden="true">
      <defs>
        <linearGradient id="footerFill" x1="0" y1="0" x2="0" y2="1">
          <stop offset="0" stop-color="#061a0c"/>
          <stop offset="0.45" stop-color="#0d3d24"/>
          <stop offset="1" stop-color="#1f9a76"/>
        </linearGradient>
      </defs>
      <path d="M0,18 Q180,-6 410,44 L410,300 L0,300 Z" fill="#1fa07c"/>
      <path d="M0,28 Q180,4 410,54 L410,300 L0,300 Z" fill="url(#footerFill)"/>
    </svg>

    <p class="journey">Start your journey to<br>health and wellness</p>
    <p class="transform">Transform your life</p>
    <div class="divider"></div>
    <p class="contact">www.harborbloomco.com.au<br>Marisol@harborbloomco.com.au</p>
    <p class="tagline-band">Natural . Raw. Organic . Cleansing system</p>
  </article>
</body>
</html>
```